Wordpress Design Project

We need a wordpress design for a new creative innovation company based in Melbourne called Quillbarrow.
We develop innovative growth and communication strategies for our clients who are generally medium sized businesses wanting to find new ways to grow their businesses.
Our Services include:
Business Strategy
Communications and Strategic Planning
Creative Consultancy
Professional Development
Change Management
Project Management
We would like our wordpress design to be simple and professional yet give a feeling of innovation, kind of like old meeting new.
We are leaning towards the predominant background colour being white, but open to suggestions.
Attached are logo files.
If you require any further information please contact us via the Marble Yard site.

```html
<!DOCTYPE html>
<html lang="en">
<head>
<meta charset="utf-8">
<title>Quillbarrow</title>
<link href="https://fonts.googleapis.com/css2?family=Ubuntu:wght@400;500;700&family=Roboto:ital,wght@0,400;0,700;1,700&display=swap" rel="stylesheet">
<style>
:root{
  --lime:#c2e01c;
  --lime-deep:#a9c71a;
  --olive:#7b8b1f;
  --olive-dark:#4f5a12;
  --card:rgba(128,140,30,.55);
  --ring:#cfe840;
  --ink:#1d1d1b;
  --grey:#555;
  --accent:#8aa012;
  --footer:#5b6170;
  --footer-dark:#4a4f5b;
  --field:#434854;
  --footer-text:#c9ccd3;
  --footer-head:#8f95a3;
}
*{box-sizing:border-box;margin:0;padding:0}
html,body{width:1038px;height:1200px;overflow:hidden}
body{position:relative;background:#fff;font-family:Roboto,Arial,sans-serif;color:var(--grey)}
.abs{position:absolute}
.top-bar{left:0;top:0;width:1038px;height:31px;background:var(--olive)}
.search{left:130px;top:4px;width:194px;height:22px;border-radius:5px;background:var(--olive-dark);box-shadow:inset 0 1px 3px rgba(0,0,0,.4)}
.search-btn{right:2px;top:2px;width:19px;height:18px;border-radius:4px;background:#c9e23a}
.call{right:130px;top:7px;font-family:Ubuntu,sans-serif;font-weight:500;font-size:13px;color:#fff}
.stage{left:0;top:31px;width:1038px;height:661px;background:radial-gradient(ellipse at 50% 30%,#cfec1f 0%,var(--lime) 45%,var(--lime-deep) 100%)}
.masthead{left:130px;top:42px;width:778px;height:76px;background:#050505;border-top:3px solid #2a2a2a}
.brand{left:14px;top:18px;font-family:Ubuntu,sans-serif;font-size:35px;color:#9ec12a;letter-spacing:-1px}
.nav{right:0;top:0;height:73px;display:flex}
.nav a{display:flex;align-items:center;padding:0 13px;font:700 9.5px Arial,sans-serif;color:#bbb;text-decoration:none;border-left:1px solid #2b2b2b;letter-spacing:.2px}
.nav a:first-child{border-left:0}
.nav a.current{color:#ddd}
.hero-title{left:138px;top:195px;font-family:Ubuntu,sans-serif;font-weight:700;font-size:32px;line-height:42px;color:var(--ink)}
.hero-art{left:535px;top:178px;width:341px;height:199px;border-radius:40%;background:radial-gradient(ellipse,#b88a5e 0%,rgba(176,140,80,.5) 50%,rgba(194,224,28,0) 75%)}
.dots{left:487px;top:413px;display:flex;gap:5px}
.dots i{width:12px;height:12px;border-radius:50%;background:#111}
.dots i.on{background:#dfe9b0;border:2px solid #9ab01a}
.card{top:472px;height:220px;background:var(--card);border-radius:8px 8px 0 0}
.ring{left:50%;top:20px;width:84px;height:84px;margin-left:-42px;border:2px solid var(--ring);border-radius:50%;display:flex;align-items:center;justify-content:center}
.card p{position:absolute;left:4px;right:4px;top:121px;font:10px/11.8px Arial,sans-serif;color:#fff;text-align:center}
.card-title{top:704px;font-family:Ubuntu,sans-serif;font-weight:500;font-size:14px;color:#6b6b6b;text-align:center;letter-spacing:.3px}
.card-title::after{content:"";display:block;margin:8px auto 0;width:150px;height:6px;border-radius:50%;background:radial-gradient(ellipse,rgba(0,0,0,.18),rgba(0,0,0,0) 70%)}
.photo-frame{left:131px;top:766px;width:197px;height:171px;border:1px solid #ddd;background:#fff}
.photo{left:8px;top:8px;width:179px;height:153px;background:linear-gradient(180deg,#e4e4e4,#cfd1d3)}
.h2{font-family:Ubuntu,sans-serif;font-weight:500;font-size:20px;color:#222}
.rule{height:1px;background:#e2e2e2}
.lead{font:700 11px/14px Arial,sans-serif;color:var(--accent)}
.body-copy{font:10px/11.8px Arial,sans-serif;color:#333}
.arrows{left:861px;top:764px;display:flex;gap:1px}
.arrows span{width:23px;height:22px;background:#1f1f1f;color:#fff;font-size:9px;display:flex;align-items:center;justify-content:center}
.arrows span.next{color:#e06b2a}
.quote{font:italic 700 11px/13.5px Roboto,Arial,sans-serif;color:#333}
.footer{left:0;top:967px;width:1038px;height:207px;background:var(--footer)}
.sep{top:985px;width:1px;height:183px;background:#474c57}
.f-head{top:980px;font-family:Ubuntu,sans-serif;font-weight:500;font-size:14px;color:var(--footer-head)}
.f-links{top:1010px;list-style:none;font:9.5px/21px Arial,sans-serif;color:var(--footer-text)}
.field{left:668px;width:210px;border-radius:10px;background:var(--field);font:9.5px Arial,sans-serif;color:#d4d6dc;padding:5px 12px}
.submit{left:803px;top:1118px;width:73px;height:26px;border-radius:13px;background:#3b404b;border:2px solid #2f333c;font:700 11px Arial,sans-serif;color:#e4e6ea;display:flex;align-items:center;justify-content:center}
.bottom{left:0;top:1174px;width:1038px;height:26px;background:var(--footer-dark);font:9px/26px Arial,sans-serif;color:#9ca1ac;text-align:center}
</style>
</head>
<body>

<div class="abs top-bar"></div>
<div class="abs search"><div class="abs search-btn">
<svg width="19" height="18" viewBox="0 0 19 18"><circle cx="11" cy="7" r="3.5" fill="none" stroke="#222" stroke-width="1.6"/><line x1="8.5" y1="9.5" x2="5" y2="13" stroke="#222" stroke-width="2"/></svg>
</div></div>
<div class="abs call">CALL US:(XXX) XXX - XXXX</div>

<div class="abs stage"></div>

<header class="abs masthead">
  <div class="abs brand">Quillbarrow</div>
  <nav class="abs nav">
    <a class="current">HOME</a><a>ABOUT US</a><a>SERVICES</a><a>TESTIMONIALS</a><a>BLOG</a><a>CONTACT US</a>
  </nav>
</header>

<h1 class="abs hero-title">OUR WORK IS DEDICATED<br>TO THE PROSPERITY OF<br>OUR CLIENTS!</h1>
<div class="abs hero-art" role="img" aria-label="Two cupped hands around a young seedling growing from soil"></div>
<div class="abs dots"><i></i><i class="on"></i><i></i><i></i></div>

<section class="abs card" style="left:130px;width:240px">
  <div class="abs ring"><svg width="30" height="44" viewBox="0 0 30 44"><path d="M15 2a12 12 0 0 0-8 21c2 2 3 4 3 7h10c0-3 1-5 3-7A12 12 0 0 0 15 2z" fill="#1e2a1a"/><rect x="10" y="32" width="10" height="2" fill="#1e2a1a"/><rect x="10" y="35" width="10" height="2" fill="#1e2a1a"/><rect x="11" y="38" width="8" height="2" fill="#1e2a1a"/></svg></div>
  <p>Lorem ipsum dolor sit amet, consectetur adipisicing elit, sed do eiusmod tempor incididunt ut labore et dolore magna aliqua. Ut enim ad minim veniam, quis nostrud exercitation ullamco laboris nisi ut aliquip ex ea commodo consequat. Duis aute irure dolor in reprehenderit in voluptate velit esse cillum dolore eu fugiat nulla pariatur.</p>
</section>
<section class="abs card" style="left:397px;width:245px">
  <div class="abs ring"><svg width="34" height="34" viewBox="0 0 34 34"><path d="M4 8h14v3H7v16h16V17h3v13H4z" fill="#1e2a1a"/><path d="M26 3l5 5-13 13-6 1 1-6z" fill="#1e2a1a"/></svg></div>
  <p>Lorem ipsum dolor sit amet, consectetur adipisicing elit, sed do eiusmod tempor incididunt ut labore et dolore magna aliqua. Ut enim ad minim veniam, quis nostrud exercitation ullamco laboris nisi ut aliquip ex ea commodo consequat. Duis aute irure dolor in reprehenderit in voluptate velit esse cillum dolore eu fugiat nulla pariatur.</p>
</section>
<section class="abs card" style="left:667px;width:240px">
  <div class="abs ring"><svg width="36" height="36" viewBox="0 0 36 36"><g fill="#1e2a1a"><circle cx="18" cy="18" r="11"/><rect x="15" y="2" width="6" height="32" rx="1"/><rect x="2" y="15" width="32" height="6" rx="1"/><rect x="15" y="2" width="6" height="32" rx="1" transform="rotate(45 18 18)"/><rect x="15" y="2" width="6" height="32" rx="1" transform="rotate(-45 18 18)"/></g><circle cx="18" cy="18" r="4.5" fill="#8c9d28"/></svg></div>
  <p>Lorem ipsum dolor sit amet, consectetur adipisicing elit, sed do eiusmod tempor incididunt ut labore et dolore magna aliqua. Ut enim ad minim veniam, quis nostrud exercitation ullamco laboris nisi ut aliquip ex ea commodo consequat. Duis aute irure dolor in reprehenderit in voluptate velit esse cillum dolore eu fugiat nulla pariatur.</p>
</section>

<div class="abs card-title" style="left:160px;width:183px">BUSINESS STRATEGY</div>
<div class="abs card-title" style="left:400px;width:233px">PROFESSIONAL DEVELOPMENT</div>
<div class="abs card-title" style="left:690px;width:193px">PROJECT MANAGEMENT</div>

<div class="abs photo-frame"><div class="abs photo" role="img" aria-label="Businessman beside a whiteboard with a sketched light bulb"></div></div>

<h2 class="abs h2" style="left:333px;top:763px">WELCOME TO OUR SITE</h2>
<div class="abs rule" style="left:333px;top:793px;width:307px"></div>
<p class="abs lead" style="left:333px;top:801px;width:310px">Sed ut perspiciatis unde omnis iste natus error sit volup-tatem accusantium doloremque</p>
<p class="abs body-copy" style="left:333px;top:841px;width:310px">inventore veritatis et quasi architecto beatae vitae dicta sunt exabo. Ne enim ipsam voluptatem quia voluptas sit aspernatur aut odit afugit, sed quia consequuntur magni dolores eos ratione voluptatem on numquam eius modi tempora incidunt ut labore et dolore magnam ali ilam quaerat voluptaUt enim ad minima veniam, quis nostrum exercitationlo corporis suscipit laboriosam, nisi ut aliquid ex ea commodi consequatureum iure reprehenderit qui in ea voluptate velit esse quam nihil molestia vel illum qui dolorem eum fugiat quo voluptas nulla pariatur</p>

<h2 class="abs h2" style="left:667px;top:763px">TESTIMONIALS</h2>
<div class="abs arrows"><span>&#9664;</span><span class="next">&#9654;</span></div>
<div class="abs rule" style="left:667px;top:793px;width:242px"></div>
<p class="abs lead" style="left:667px;top:800px;font-style:italic">Phasellus porta fusce suscipit varius</p>
<p class="abs quote" style="left:667px;top:828px;width:230px">“ Molestie lacus. Aenean nonummy hen-drerit mauris. Phasellus porta. Fusce suscipit varius mi. Cum sociis natoque penatibus et magnis dis parturient montes, nascetur ridiculus mus. Nulla dui.”</p>
<p class="abs lead" style="left:820px;top:923px;font-style:italic">- Mara Ellison</p>

<footer class="abs footer"></footer>
<div class="abs sep" style="left:352px"></div>
<div class="abs sep" style="left:637px"></div>
<h3 class="abs f-head" style="left:138px">INFORMATION</h3>
<ul class="abs f-links" style="left:139px"><li>About Us</li><li>Sitemap</li><li>FAQ</li><li>Privacy Policy</li><li>T&amp;C</li><li>Contact US</li></ul>
<h3 class="abs f-head" style="left:397px">INFORMATION</h3>
<ul class="abs f-links" style="left:398px"><li>Business Strategy</li><li>Communications and Strategic Planning</li><li>Creative Consultancy</li><li>Professional Development</li><li>Change Management</li><li>Project Management</li></ul>
<h3 class="abs f-head" style="left:667px">GET IN TOUCH</h3>
<div class="abs field" style="top:1011px;height:21px">Name</div>
<div class="abs field" style="top:1036px;height:21px">Email</div>
<div class="abs field" style="top:1062px;height:49px;padding-top:9px">Message</div>
<div class="abs submit">SUBMIT</div>

<div class="abs bottom">© 2012 Quillbarrow. All Rights Reserved.</div>

</body>
</html>
```